Mobile Repair Service on location needs a Web Design

We are starting a new mobile device repair service called Gadget Haven and our website needs a design!

Hello Designers!
First, we'd like to make clear this is more than a simple web design contest, we want the designers to create an idea. We want someone who can create the whole theme of the service's we provide. We want someone that can help design our visual branding, help us communicate a sentiment. And we are willing to pay for that.

Who are we?
Our company is based in Rotterdam, the Netherlands. We provide different services for all kinds of electronic devices. The kind of services we provide are, among other things, installations of hardware and software and the repair of broken or malfunctioning devices.
We are starting a new service that offers mobile device repairs on location, be it at the home of our customers, their office, or any other place. Just give us the address and we will come to you for the repair job. This is also our main USP. We have multiple skilled engineers who drive trough the country on a daily basis and can be on location within a working day. Repair is done immediately onsite while the customer waits. At this stage we will start with the smartphone product-group within the mobile devices. In a second phase we might also add tablets.
People don't want to be without their phone for weeks because of some parts that needed to be ordered by a repair center they had to sent their phone to. We offer a fully functional mobile repair center in the form of specially customized vans. These vans have all the tools and utilities needed by our engineers to safely repair your mobile device. Your phone is being repaired directly in front of you, the next business-day, on a location you desire.

For this new service we are creating a website called Gadget Haven. The website needs a story and matching design and this is where you come in. We are not looking for a simple template design we can get from any place. We need a story. We want you to create an idea, build a unique theme or vision that helps sell the product/service. This goes beyond the design of the website. We need the whole package, the design you are creating needs to have returning elements like icons, color use, images, maybe even characters etc. You name it! There needs to be a common thread in the design so we can reuse elements in, for example, the email templates, the work order or receipt we give to our customers (we may contact the winner of the contest to design these for us as well!).

The name 'Gadget Haven' is chosen. Haven (short for rehabilitate) has a bold and playful tone to it and the design needs to reflect the name. So we're looking for a somewhat playful and cheeky design. Definitely not too serious and definitely modern. We already got a logo that we love and that fit's this description (see attached design documents for the logo). It's bold, powerful and fun. Our web design needs to reflect this as well and has to fit in with our logo.
We would really like it if the design somehow incorporates elements that highlight our unique selling points (repairs on location, we come to you etc.). We would really like some form of story telling in the design. Think clumsy people breaking their phones. Teenagers in tears because they have no access to their friends. People nowadays have the need to always be 'connected'. What happens when your phone is broken or malfunctioning? We're handling tech, we are nerds and a little bit weird, but we're professionals and here to help you with your problem. The sentiment Wire Troop tries to communicate is something we really like. We're looking for fresh idea's, anything goes!

In an overview all Unique Selling Points of the Gadget haven service:
- Professional service on location. Don’t ship to us we will come to you!
- Clear pricing upfront. No hidden cost.
- Next business-day repair.
- Backed by a professional call center open 12 hours a day and open on a Saturday as well
- Backed by a professional repair center with more then 12 years of experience
- Repair is done by certified engineers
- 1 year warranty on the repair

The process:
The main function of our website will be for customers to make a repair request. A customer will visit our website and can make a repair request immediately by going through a 'request-order-flow'. In this flow he or she will need to fill in some forms and can select wich type/model/brand of mobile device he or she has and what parts need to be repaired. After a request is placed we will call the customer back (within an hour) for a short intake and to set a date/time and location. Our engineer will meet the customer at the specified location and will repair the device onsite in one of our mobile repair centers, which is a specialized van equipped with all the tools needed for device restorations.
So in short the steps are:
- Choose your device and repair job
- Place the order
- Get a callback within the hour
- Set date and location
- We will come to you.

Website functionality:
Our website is our main form of communication. So the sentiment we want to communicate needs be reflected in the design. We need a main/front page designed (preferably a long scrolling page design) containing:
1. Customers will be able to request a repair job directly on our website. So there will need to be a prominent button/link at the top of our main page that will bring the customer to this 'request-order-flow'. This is the main flow which needs to be full focus on the front page. All other items are secondary.
2. The general information of who we are and what we do, and why the customer should choose us. Preferably in short bullet-point type keywords/sentences with icons or other visual cues. See our unique selling points to get an idea of the information that will be displayed here.
3. There needs to be a section that will explain the process (see above) of a repair request step-by- step, again in brief short key sentences and with (custom) icons.
4. There needs to be a section that explains to the customer he/she can always contact us if they are not sure what the problem is with their device, and for this reason are not sure what repair request they should order.
5. We want to implement some functionality that display customer ratings or customer reviews. So there needs to be room for some kind of widget of plugin we're going to implement which shows these reviews.
6. A 'For business section' where we will explain all the options we provide for corporate clients.
7. Social media links.
8. There needs to be a menu with buttons that leads to the all sections described in the previous points.

For now, we need a design for our front page. In the second phase, when we have picked our winner, we may ask the winner to design the page(s) for our request workflow as well.

EDIT:
Finally, we have a very specific order in mind for the different segments of our website. We would like you to add some more segments that were not in our original brief as well:

1. Top header with order/request button. (should instantly make clear our main USP, we do repairs on location)
2. Our process
3. Our unique selling points / why choose us
4. The kind of repairs we do (broken screens, broken batteries, water damage, broken camera's, no sound etc.)
5. A 'meet our team' section, where we introduce some of our engineers
6. A 'contact us for any questions' section/
7. Testimonials/user reviews
8. A section where we show key performance indicators
9. 'For businesses' sections
10.'Subscribe for newsletter' field
11. Social media buttons

Industry/Entity Type

It Service

Number of Pages Required

1 page

Font styles to use
Sans Serif

Requirements
Must have
• a main/front page, design only
• custom icons/images for banners, adverts online and in print (high res)
Nice to have
• Storytelling in our design.
• Design that fits with our brand new logo.
• Elements like icons to have a flat design.
• Keep in mind that the website will need to be responsive when designing! (Ideally provide an example of the mobile design as well)
• Create a fun and trustworthy feeling.

```html
<!DOCTYPE html>
<html lang="en">
<head>
<meta charset="utf-8">
<title>Gadget Haven – Mobile Repair On Location</title>
<link rel="stylesheet" href="https://fonts.googleapis.com/css2?family=Raleway:wght@300;400;600;700;800&family=Open+Sans:wght@400;600;700&display=swap">
<style>
:root{
  --orange:#f15a24;
  --ink:#222;
  --text:#555;
  --muted:#8a8a8a;
  --line:#dcdcdc;
  --dark:#1c1c1c;
  --darker:#141414;
  --pale:#ededed;
  --white:#fff;
}
*{box-sizing:border-box;margin:0;padding:0}
html,body{width:1200px;height:4986px;overflow:hidden}
body{font-family:"Open Sans",Arial,sans-serif;color:var(--text);background:var(--white);font-size:14px;line-height:1.6}
h1,h2,h3,h4{font-family:"Raleway",Arial,sans-serif}
.wrap{width:1060px;margin:0 auto;position:relative}
.btn{display:inline-block;background:var(--orange);color:var(--white);font-family:"Raleway",sans-serif;font-weight:600;font-size:15px;padding:10px 26px;border-radius:22px;text-decoration:none}
.section-title{text-align:center;color:var(--ink);line-height:1.15}
.section-title .light{display:block;font-weight:300;font-size:32px}
.section-title .bold{display:block;font-weight:700;font-size:32px}
.section-title::after{content:"";display:block;width:44px;height:3px;background:var(--orange);margin:12px auto 0}
.photo{display:block}

/* header */
.site-header{height:110px}
.site-header .wrap{height:110px;display:flex;align-items:center;justify-content:space-between}
.brand{display:flex;align-items:center;gap:10px;font-family:"Raleway",sans-serif;font-weight:800;font-size:24px;color:var(--ink);line-height:1}
.brand .dot{width:30px;height:30px;border-radius:50%;background:var(--orange)}

/* hero */
.hero{height:605px;position:relative;clip-path:polygon(0 0,100% 0,100% 93%,0 100%)}
.hero .photo{position:absolute;inset:0;background:linear-gradient(120deg,#3a3f46 0%,#6d6a66 45%,#8d8479 70%,#b7aa9b 100%)}
.hero .shade{position:absolute;inset:0;background:rgba(10,10,10,.45)}
.hero .content{position:relative;text-align:center;color:var(--white);padding-top:170px}
.hero h1{font-weight:400;font-size:46px;line-height:1.2}
.hero p{width:780px;margin:26px auto 30px;font-size:16px;line-height:1.7}

/* process */
.process{height:515px;padding-top:70px}
.steps{display:flex;justify-content:space-between;margin-top:46px}
.step{width:180px;text-align:center}
.step .photo{width:110px;height:130px;margin:0 auto 16px;border-radius:8px;background:linear-gradient(180deg,#f3f3f3,#e2e2e2)}
.step h3{color:var(--orange);font-family:"Open Sans",sans-serif;font-weight:600;font-size:15px;line-height:1.35;margin-bottom:10px}
.step p{font-size:12px;color:var(--muted);line-height:1.5}

/* what we do */
.what{height:550px;position:relative;color:var(--white)}
.what .photo{position:absolute;inset:0;background:linear-gradient(100deg,#e8501c 0%,#f26a2c 45%,#f7934f 75%,#f06228 100%)}
.what .inner{position:relative;padding-top:80px}
.what .section-title{color:var(--white)}
.what .section-title::after{background:var(--white)}
.usps{display:flex;justify-content:space-between;margin-top:50px;position:relative}
.usps::before{content:"";position:absolute;left:40px;right:40px;top:58px;height:2px;background:rgba(255,255,255,.6)}
.usp{width:140px;text-align:center;position:relative}
.usp .ring{width:116px;height:116px;border-radius:50%;background:#d8d5df;margin:0 auto;display:flex;align-items:center;justify-content:center}
.usp .core{width:84px;height:84px;border-radius:50%;background:#2d2d33;display:flex;align-items:center;justify-content:center}
.usp h3{font-family:"Open Sans",sans-serif;font-weight:700;font-size:14px;line-height:1.35;margin-top:26px}
.usp p{font-size:11px;line-height:1.45;margin-top:4px}

/* why */
.why{height:515px;padding-top:80px}
.why .intro{width:920px;margin:40px auto 34px;text-align:center;font-size:14px;line-height:1.75}
.ticks{display:grid;grid-template-columns:1fr 1fr;column-gap:60px;row-gap:14px;width:960px;margin:0 auto}
.ticks li{list-style:none;display:flex;align-items:center;gap:12px;font-size:14px;padding-bottom:12px;border-bottom:1px solid #eee}

/* team */
.team{height:515px;position:relative;color:var(--white)}
.team .photo-bg{position:absolute;inset:0;background:linear-gradient(90deg,#1d1d1d,#343230 50%,#1e1e1e)}
.team .inner{position:relative;padding-top:60px}
.team-head{display:flex;gap:40px}
.team-head h2{font-weight:800;font-size:38px;line-height:1;white-space:nowrap}
.team-head .years{font-size:16px;margin-top:8px}
.team-head p{font-size:16px;line-height:1.6;width:640px}
.members{display:flex;justify-content:space-between;margin-top:50px}
.member{width:196px;background:var(--white);padding:10px 10px 14px}
.member .photo{height:168px;background:linear-gradient(180deg,#c9c3bb,#8e8780)}
.member h4{font-family:"Open Sans",sans-serif;color:var(--ink);font-weight:600;font-size:13px;margin-top:12px;line-height:1.2}
.member span{font-size:11px;color:var(--muted)}

/* contact */
.contact{height:530px;display:flex}
.contact .visual{width:600px;height:530px;background:linear-gradient(135deg,#9da3a9,#d7d9dc 55%,#b4b8bc)}
.contact .form{flex:1;padding:90px 0 0 160px}
.contact h2{font-weight:300;font-size:32px;color:var(--ink);line-height:1.15}
.contact h2 b{display:block;font-weight:700}
.field{width:330px;border-bottom:1px solid var(--line);font-size:14px;padding:16px 0 8px;color:var(--text)}
.field:first-of-type{margin-top:24px}
.field i{color:var(--orange);font-style:normal;margin-right:4px}
.contact .btn{margin-top:34px}

/* testimonials */
.testimonials{height:365px;padding-top:60px}
.quotes{display:flex;justify-content:space-between;margin-top:44px}
.quote{width:490px;display:flex;gap:20px;align-items:flex-start}
.quote .photo{width:110px;height:110px;border-radius:50%;border:4px solid var(--orange);background:linear-gradient(180deg,#d4c6bc,#9d8d82);flex:none}
.quote blockquote{font-size:13px;line-height:1.6;padding-top:14px;position:relative;padding-left:36px}
.quote blockquote::before{content:"\201C";position:absolute;left:0;top:0;font-size:56px;color:var(--ink);line-height:1;font-family:Georgia,serif}
.quote cite{display:block;color:var(--orange);font-style:normal;margin-top:12px}

/* kpi */
.kpi{height:615px;background:var(--pale);padding-top:60px;position:relative}
.kpi .photo{position:absolute;left:350px;top:200px;width:500px;height:400px;background:radial-gradient(ellipse at center,#cdd3d9 0%,#e4e6e8 60%,var(--pale) 100%);border-radius:20px}
.cloud{position:absolute;width:300px;height:150px;background:var(--white);border-radius:75px;display:flex;align-items:center;gap:18px;padding:0 30px}
.cloud .badge{width:64px;height:64px;border-radius:50%;background:var(--white);border:3px solid var(--orange);display:flex;align-items:center;justify-content:center;flex:none;font-weight:700;color:var(--ink);font-size:17px}
.cloud p{font-size:15px;font-weight:700;color:var(--ink);line-height:1.35}
.cloud.tl{left:140px;top:190px}.cloud.tr{right:140px;top:190px}
.cloud.bl{left:140px;top:420px}.cloud.br{right:140px;top:420px}

/* business */
.business{height:265px;padding-top:70px}
.business .wrap{display:flex;align-items:flex-start}
.business h2{width:220px;text-align:center;font-weight:300;font-size:30px;color:var(--ink);line-height:1.15;padding-top:34px;border-right:2px solid var(--line);height:130px}
.business h2 b{display:block;font-weight:700}
.business .list{padding-left:60px}
.business h3{font-weight:600;font-size:28px;color:var(--orange);margin-bottom:12px}
.business li{list-style:none;color:var(--orange);font-size:15px;line-height:1.9}
.business li::before{content:"\25A0";font-size:9px;margin-right:10px;vertical-align:middle}

/* footer */
.site-footer{height:401px;background:var(--dark);color:#c9c9c9;position:relative}
.site-footer .cols{display:flex;justify-content:space-between;padding-top:40px}
.site-footer h4{color:var(--orange);font-weight:600;font-size:17px;margin-bottom:18px}
.site-footer ul{list-style:none;font-size:13px;line-height:1.95}
.site-footer ul li::before{content:"\203A";color:var(--orange);margin-right:8px}
.col-contact p{font-size:13px;line-height:1.6;margin-bottom:10px}
.col-news p{font-size:13px;width:240px;margin-bottom:12px}
.col-news .input{width:240px;height:30px;background:var(--white);font-size:12px;color:#999;padding:5px 10px}
.col-news .sub{display:inline-block;background:var(--orange);color:var(--white);font-size:12px;padding:4px 14px;margin-top:12px}
.social li{display:flex;align-items:center;gap:10px;margin-bottom:8px}
.social li::before{content:none}
.social .sq{width:24px;height:24px;background:#3a3a3a;border-radius:3px}
.copyright{position:absolute;left:0;right:0;bottom:0;height:36px;background:var(--darker);text-align:center;font-size:12px;line-height:36px;color:#999}
</style>
</head>
<body>

<header class="site-header">
  <div class="wrap">
    <div class="brand"><span class="dot"></span>Gadget Haven</div>
    <a class="btn" href="#request">Request a Repair</a>
  </div>
</header>

<section class="hero">
  <div class="photo" role="img" aria-label="Photograph of a technician repairing a smartphone at a workbench with tools"></div>
  <div class="shade"></div>
  <div class="content">
    <h1>Best Mobile Repair Service<br>At Any Time In Anywhere</h1>
    <p>We are starting a new service that offers mobile device repairs on location, be it at the home of our customers, their office, or any other place. Just give us the address and we will come to you for the repair job.</p>
    <a class="btn" id="request" href="#">Request a Repair</a>
  </div>
</section>

<section class="process">
  <div class="wrap">
    <h2 class="section-title"><span class="light">Our</span><span class="bold">Process</span></h2>
    <div class="steps">
      <div class="step"><div class="photo" role="img" aria-label="Cartoon character choosing a phone repair"></div><h3>Choose your device<br>and repair job</h3><p>Suspendisse iaculis elit nec ornare pellentes. Donec lacinia lectus malesuada.</p></div>
      <div class="step"><div class="photo" role="img" aria-label="Cartoon character placing an order"></div><h3>Place the<br>order</h3><p>Suspendisse iaculis elit nec ornare pellentes. Donec lacinia lectus malesuada.</p></div>
      <div class="step"><div class="photo" role="img" aria-label="Cartoon character receiving a callback"></div><h3>Get a callback within<br>the hour</h3><p>Suspendisse iaculis elit nec ornare pellentes. Donec lacinia lectus malesuada.</p></div>
      <div class="step"><div class="photo" role="img" aria-label="Cartoon character holding a date and location sign"></div><h3>Set date and<br>location</h3><p>Suspendisse iaculis elit nec ornare pellentes. Donec lacinia lectus malesuada.</p></div>
      <div class="step"><div class="photo" role="img" aria-label="Cartoon engineer arriving with a phone"></div><h3>We will come<br>to you</h3><p>Suspendisse iaculis elit nec ornare pellentes. Donec lacinia lectus malesuada.</p></div>
    </div>
  </div>
</section>

<section class="what">
  <div class="photo" role="img" aria-label="Orange-tinted photograph of hands repairing a phone"></div>
  <div class="wrap inner">
    <h2 class="section-title"><span class="light">What</span><span class="bold">We Do</span></h2>
    <div class="usps">
      <div class="usp"><div class="ring"><div class="core"><svg width="40" height="40" viewBox="0 0 40 40" fill="none" stroke="#fff" stroke-width="3"><circle cx="20" cy="11" r="6"/><path d="M8 34c2-9 22-9 24 0"/></svg></div></div><h3>Professional service</h3><p>on location. Don't ship to us we will come to you!</p></div>
      <div class="usp"><div class="ring"><div class="core"><svg width="40" height="40" viewBox="0 0 40 40" fill="none" stroke="#fff" stroke-width="3"><circle cx="24" cy="13" r="7"/><path d="M4 30h10l8 4 14-8"/></svg></div></div><h3>Clear pricing upfront.</h3><p>No hidden cost.</p></div>
      <div class="usp"><div class="ring"><div class="core"><svg width="40" height="40" viewBox="0 0 40 40" fill="none" stroke="#fff" stroke-width="3"><rect x="12" y="5" width="16" height="30" rx="3"/><path d="M18 30h4"/></svg></div></div><h3>Backed by a professional call center</h3><p>open 12 hours a day and open on a Saturday as well</p></div>
      <div class="usp"><div class="ring"><div class="core"><svg width="40" height="40" viewBox="0 0 40 40" fill="none" stroke="#fff" stroke-width="3"><rect x="6" y="9" width="28" height="25" rx="2"/><path d="M6 16h28M13 5v7M27 5v7"/></svg></div></div><h3>Next business-day</h3><p>repair</p></div>
      <div class="usp"><div class="ring"><div class="core"><svg width="40" height="40" viewBox="0 0 40 40" fill="none" stroke="#fff" stroke-width="3"><path d="M8 32 28 12M28 8l4 4M12 8l20 24M8 12l4-4"/></svg></div></div><h3>Backed by a professional repair center</h3><p>with more then 12 years of experience</p></div>
      <div class="usp"><div class="ring"><div class="core"><svg width="40" height="40" viewBox="0 0 40 40" fill="none" stroke="#fff" stroke-width="3"><circle cx="14" cy="14" r="5"/><circle cx="27" cy="14" r="5"/><path d="M4 32c1-7 19-7 20 0M18 32c1-7 18-7 19 0"/></svg></div></div><h3>Repair is done</h3><p>by certified engineers</p></div>
      <div class="usp"><div class="ring"><div class="core"><svg width="40" height="40" viewBox="0 0 40 40" fill="none" stroke="#fff" stroke-width="3"><circle cx="20" cy="16" r="10"/><path d="M14 25l-3 10 9-4 9 4-3-10"/></svg></div></div><h3>1 year warranty</h3><p>on the repair</p></div>
    </div>
  </div>
</section>

<section class="why">
  <div class="wrap">
    <h2 class="section-title"><span class="light">Why</span><span class="bold">Choose Us</span></h2>
    <p class="intro">We have multiple skilled engineers who drive trough the country on a daily basis and can be on location within a working day. Repair is done immediately onsite while the customer waits. Your phone is being repaired directly in front of you, the next business-day, on a location you desire.</p>
    <ul class="ticks">
      <li><svg width="18" height="18" viewBox="0 0 18 18"><circle cx="9" cy="9" r="8" fill="none" stroke="#f15a24" stroke-width="1.5"/><path d="M5 9l3 3 5-6" fill="none" stroke="#f15a24" stroke-width="2"/></svg>Lorem ipsum dolor sit amet, consectetur adipiscing elit</li>
      <li><svg width="18" height="18" viewBox="0 0 18 18"><circle cx="9" cy="9" r="8" fill="none" stroke="#f15a24" stroke-width="1.5"/><path d="M5 9l3 3 5-6" fill="none" stroke="#f15a24" stroke-width="2"/></svg>Lorem ipsum dolor sit amet, consectetur adipiscing elit</li>
      <li><svg width="18" height="18" viewBox="0 0 18 18"><circle cx="9" cy="9" r="8" fill="none" stroke="#f15a24" stroke-width="1.5"/><path d="M5 9l3 3 5-6" fill="none" stroke="#f15a24" stroke-width="2"/></svg>Nulla justo erat, vehicula vitae tortor quis, sodales</li>
      <li><svg width="18" height="18" viewBox="0 0 18 18"><circle cx="9" cy="9" r="8" fill="none" stroke="#f15a24" stroke-width="1.5"/><path d="M5 9l3 3 5-6" fill="none" stroke="#f15a24" stroke-width="2"/></svg>Nulla justo erat, vehicula vitae tortor quis, sodales</li>
      <li><svg width="18" height="18" viewBox="0 0 18 18"><circle cx="9" cy="9" r="8" fill="none" stroke="#f15a24" stroke-width="1.5"/><path d="M5 9l3 3 5-6" fill="none" stroke="#f15a24" stroke-width="2"/></svg>Class aptent taciti sociosqu ad litora torquent per conubia</li>
      <li><svg width="18" height="18" viewBox="0 0 18 18"><circle cx="9" cy="9" r="8" fill="none" stroke="#f15a24" stroke-width="1.5"/><path d="M5 9l3 3 5-6" fill="none" stroke="#f15a24" stroke-width="2"/></svg>Class aptent taciti sociosqu ad litora torquent per conubia</li>
      <li><svg width="18" height="18" viewBox="0 0 18 18"><circle cx="9" cy="9" r="8" fill="none" stroke="#f15a24" stroke-width="1.5"/><path d="M5 9l3 3 5-6" fill="none" stroke="#f15a24" stroke-width="2"/></svg>Integer viverra, leo non dignissim blandit, est neque commodo</li>
      <li><svg width="18" height="18" viewBox="0 0 18 18"><circle cx="9" cy="9" r="8" fill="none" stroke="#f15a24" stroke-width="1.5"/><path d="M5 9l3 3 5-6" fill="none" stroke="#f15a24" stroke-width="2"/></svg>Integer viverra, leo non dignissim blandit, est neque commodo</li>
    </ul>
  </div>
</section>

<section class="team">
  <div class="photo-bg" role="img" aria-label="Dark photograph of a repair workshop"></div>
  <div class="wrap inner">
    <div class="team-head">
      <div><h2>MEET THE TEAM</h2><div class="years">We have +10 years Experience</div></div>
      <p>We have multiple skilled engineers who drive trough the country on a daily basis and can be on location within a working day. Repair is done immediately onsite while the customer waits. Your phone is being repaired directly in front of you, the next business-day, on a location you desire.</p>
    </div>
    <div class="members">
      <div class="member"><div class="photo" role="img" aria-label="Portrait photo of an engineer"></div><h4>ALEX BRANDT</h4><span>SENIOR TECHNICIAN</span></div>
      <div class="member"><div class="photo" role="img" aria-label="Portrait photo of an engineer"></div><h4>ALEX BRANDT</h4><span>SENIOR TECHNICIAN</span></div>
      <div class="member"><div class="photo" role="img" aria-label="Portrait photo of an engineer"></div><h4>ALEX BRANDT</h4><span>SENIOR TECHNICIAN</span></div>
      <div class="member"><div class="photo" role="img" aria-label="Portrait photo of an engineer"></div><h4>ALEX BRANDT</h4><span>SENIOR TECHNICIAN</span></div>
      <div class="member"><div class="photo" role="img" aria-label="Portrait photo of an engineer"></div><h4>ALEX BRANDT</h4><span>SENIOR TECHNICIAN</span></div>
    </div>
  </div>
</section>

<section class="contact">
  <div class="visual" role="img" aria-label="Photograph of a hand holding out a company business card"></div>
  <div class="form">
    <h2>Contact Us<b>For Any Questions</b></h2>
    <div class="field"><i>*</i>First Name</div>
    <div class="field"><i>*</i>Last Name</div>
    <div class="field"><i>*</i>Email Address</div>
    <div class="field"><i>*</i>Phone Number</div>
    <a class="btn" href="#">Request a Repair</a>
  </div>
</section>

<section class="testimonials">
  <div class="wrap">
    <h2 class="section-title"><span class="light">Client</span><span class="bold">Testimonials</span></h2>
    <div class="quotes">
      <div class="quote"><div class="photo" role="img" aria-label="Customer portrait photo"></div><blockquote>Donec turpis turpis, dapibus sed lorem vel, condimentum ultrices sem leo magna condimentum nulla.<cite>– Mira Kovac</cite></blockquote></div>
      <div class="quote"><div class="photo" role="img" aria-label="Customer portrait photo"></div><blockquote>Donec turpis turpis, dapibus sed lorem vel, condimentum ultrices sem leo magna condimentum nulla.<cite>– Tomas Berg</cite></blockquote></div>
    </div>
  </div>
</section>

<section class="kpi">
  <h2 class="section-title"><span class="light">Key</span><span class="bold">Performance</span></h2>
  <div class="photo" role="img" aria-label="Illustration of hands repairing a circuit board with tools around"></div>
  <div class="cloud tl"><div class="badge"><svg width="30" height="30" viewBox="0 0 30 30" fill="none" stroke="#f15a24" stroke-width="2.5"><circle cx="15" cy="10" r="5"/><path d="M5 27c2-8 18-8 20 0"/></svg></div><p>We have experienced team</p></div>
  <div class="cloud tr"><div class="badge">95%</div><p>Customers are happy with our service</p></div>
  <div class="cloud bl"><div class="badge"><svg width="30" height="30" viewBox="0 0 30 30" fill="none" stroke="#f15a24" stroke-width="2.5"><rect x="9" y="3" width="12" height="24" rx="2"/><path d="M13 23h4"/></svg></div><p>We provide original gadgets</p></div>
  <div class="cloud br"><div class="badge">$</div><p>We provide service in the reasonable price</p></div>
</section>

<section class="business">
  <div class="wrap">
    <h2>For<b>Business</b></h2>
    <div class="list">
      <h3>The services we provide for corporate clients are-</h3>
      <ul>
        <li>In nec orci at diam sollicitudin mollis.</li>
        <li>Nunc venenatis ligula id purus varius, quis dapibus erat auctor.</li>
        <li>Suspendisse in diam vitae ex commodo commodo.</li>
      </ul>
    </div>
  </div>
</section>

<footer class="site-footer">
  <div class="wrap cols">
    <div class="col-links">
      <h4>Quick Links</h4>
      <ul><li>Home</li><li>Who We Are</li><li>What We Do</li><li>Our Process</li><li>Pricing</li><li>Testimonials</li><li>Our Clients</li><li>Contact Us</li></ul>
    </div>
    <div class="col-contact">
      <h4>Contact Information</h4>
      <p>Lorem ipsum dolor sit amet<br>consectetur adipiscing elit</p>
      <p>Sed do eiusmod tempor<br>incididunt ut labore</p>
      <p>info@gadgethaven.com</p>
    </div>
    <div class="col-news">
      <h4>Newsletter Signup</h4>
      <p>Please enter your email address below to receive our FREE newsletter</p>
      <div class="input">Your E-mail</div>
      <span class="sub">Subscribe</span>
    </div>
    <div class="col-follow">
      <h4>Follow Us</h4>
      <ul class="social">
        <li><span class="sq"></span>Facepage</li>
        <li><span class="sq"></span>Linkup</li>
        <li><span class="sq"></span>Chirper</li>
        <li><span class="sq"></span>Email</li>
      </ul>
    </div>
  </div>
  <div class="copyright">Copyright 2016 gadgethaven.com. All Rights Are Reserved.</div>
</footer>

</body>
</html>
```